Need webpage for TUTORING COMPANY

Hello,
Our tutoring company Quillbrook Tutorials is launching a new program named 'Daylight Walk-Home Program'.
We would like a website created to showcase our new program.
Our current company page is: www.quillbrook.org
The new program webpage can have a link on the current company page that takes you to the new program webpage. We are open to ideas in regards to this. I would like the new program page to have the following:
-student online registration
-a way for parents to schedule their calendar days for the program
-a way for parents to pay (pricing is $45 a day or $745 per month)
The web content will be similar to this: http://pebblecoveclubhouse.com/
I personally did not like their website and I prefer a modern, sleek, structured, eye catchy design.
We need the website fairly quickly.
Thank you,
Varsha Menon
P.S: I am attaching the flyer & brochure for the new program.
School
After School Program by QuillBrook Tutoriails

```html
<!DOCTYPE html>
<html lang="en">
<head>
<meta charset="utf-8">
<title>Quillbrook Tutorials — Daylight Walk-Home Program</title>
<link href="https://fonts.googleapis.com/css2?family=Open+Sans:wght@400;600;700;800&display=swap" rel="stylesheet">
<style>
:root{
  --ink:#111;
  --coal:#1b1b1b;
  --panel:#232323;
  --yellow:#f6c417;
  --orange:#f08a1c;
  --blue:#3b7dd8;
  --teal:#21a3a3;
  --muted:#9a9a9a;
  --light:#e6e6e6;
  --white:#fff;
}
*{box-sizing:border-box;margin:0;padding:0}
html,body{width:711px;height:1200px;overflow:hidden}
body{background:var(--coal);font-family:"Open Sans",Arial,sans-serif;color:var(--light);font-size:7px;line-height:1.45}
.page{position:relative;width:711px;height:1200px;overflow:hidden}

/* top bar */
.topbar{height:33px;background:var(--ink);display:flex;align-items:center;justify-content:space-between;padding:0 24px}
.brand{display:flex;align-items:center;gap:6px;font-weight:800;font-size:13px;color:var(--yellow);letter-spacing:.5px;text-transform:uppercase}
.brand-mark{width:12px;height:12px;background:var(--yellow)}
.top-right{text-align:right}
.top-links{display:flex;gap:3px;justify-content:flex-end;margin-bottom:3px}
.top-links span{background:var(--orange);color:var(--white);font-size:5px;padding:1px 6px}
.call{font-weight:700;font-size:9px;color:var(--white)}

/* nav */
.nav{height:19px;background:var(--ink);border-top:1px solid #333;display:flex;align-items:center;padding:0 24px;gap:2px}
.nav a{color:var(--light);text-decoration:none;font-size:6px;padding:3px 9px}
.nav a.active{background:var(--yellow);color:var(--ink);font-weight:700}

/* hero */
.hero{position:relative;height:244px}
.hero-photo{position:absolute;inset:0;background:linear-gradient(90deg,#6b4a1e 0%,#a97a35 40%,#d9b070 70%,#8c6a3a 100%)}
.hero-shade{position:absolute;inset:0;background:linear-gradient(90deg,rgba(0,0,0,.55),rgba(0,0,0,0) 55%)}
.hero-text{position:absolute;left:42px;top:118px}
.hero-text h1{font-size:20px;font-weight:700;color:var(--white);line-height:1.2}
.hero-text p{font-size:8px;color:var(--yellow);margin-top:3px}
.btn{display:inline-block;background:var(--orange);color:var(--white);font-size:6px;padding:3px 9px;margin-top:7px}
.hero-rule{height:5px;background:var(--yellow)}

/* services */
.services{height:293px;background:radial-gradient(ellipse at 50% 30%,#2e2e2e,#141414 75%);text-align:center;padding-top:68px}
.section-title{font-size:13px;font-weight:800;color:var(--yellow);text-transform:uppercase}
.services .sub{font-size:7px;font-weight:700;color:var(--white);text-transform:uppercase;margin-top:2px}
.service-grid{display:flex;justify-content:center;gap:30px;margin-top:30px}
.service{width:118px}
.service-icon{width:32px;height:32px;margin:0 auto;display:flex;align-items:center;justify-content:center}
.service-icon svg{width:18px;height:18px}
.i-yellow{background:var(--yellow)}
.i-blue{background:var(--blue)}
.i-orange{background:var(--orange)}
.i-teal{background:var(--teal)}
.service h3{font-size:7px;font-weight:700;color:var(--yellow);text-transform:uppercase;margin-top:14px}
.service p{font-size:5.5px;color:var(--muted);margin-top:5px}
.more{display:inline-block;margin-top:8px;background:#3a3a3a;color:#bbb;font-size:5px;padding:2px 8px}

/* tutors */
.tutors{position:relative;height:183px;background:var(--coal);padding:45px 42px 0}
.tutors .section-title{color:var(--orange);text-align:left}
.tutors-body{display:flex;gap:40px;margin-top:8px}
.tutors-body p{width:420px;font-size:5.5px;color:var(--muted)}
.checks{list-style:none;font-size:5.5px;color:var(--light)}
.checks li{display:flex;align-items:center;gap:4px;margin-bottom:2px}
.checks svg{width:6px;height:6px}
.bus{position:absolute;right:6px;top:122px;width:64px;height:36px;background:linear-gradient(180deg,#f6c417,#d99e0f);border-radius:4px}
.road{position:absolute;left:0;right:0;top:158px;height:3px;background:repeating-linear-gradient(90deg,var(--yellow) 0 16px,transparent 16px 26px)}

/* become a tutor */
.tutor-bar{margin:0 42px;height:20px;background:#2f2f2f;display:flex;align-items:center;justify-content:center;font-size:7px;font-weight:700;color:var(--white);text-transform:uppercase}
.tutor-bar span{color:var(--yellow);margin-left:4px}

/* testimonials + schedule */
.lower{display:flex;gap:30px;padding:22px 42px 0;height:205px}
.lower .section-title{font-size:11px;text-align:left}
.testimonial{width:290px}
.testimonial p{font-size:5.5px;color:var(--muted);margin-top:10px}
.author{font-size:6px;font-weight:700;color:var(--yellow);margin-top:8px}
.author-role{font-size:5px;color:var(--muted)}
.schedule{flex:1}
.tabs{display:flex;margin-top:10px}
.tabs span{flex:1;text-align:center;font-size:5.5px;padding:3px 0;background:#333;color:var(--light)}
.tabs span.on{background:var(--yellow);color:var(--ink);font-weight:700}
.schedule table{width:100%;border-collapse:collapse;margin-top:4px}
.schedule td{font-size:5.5px;padding:3px 4px;border-bottom:1px solid #2c2c2c;color:var(--light)}
.schedule td.time{color:var(--yellow);width:90px}

/* footer */
.footer{position:absolute;left:0;right:0;top:995px;height:170px;background:var(--ink);display:flex;gap:40px;padding:20px 42px}
.footer h4{font-size:7px;font-weight:700;color:var(--yellow);margin-bottom:8px}
.links{display:flex;gap:24px}
.links ul{list-style:none;font-size:5.5px;color:var(--muted)}
.links li{margin-bottom:3px}
.newsletter{width:150px}
.newsletter p{font-size:5.5px;color:var(--muted)}
.field{height:12px;background:#2b2b2b;margin-top:8px;font-size:5px;color:#777;padding:2px 4px}
.submit{display:inline-block;background:var(--blue);color:var(--white);font-size:5.5px;padding:2px 8px;margin-top:4px}
.contact p{font-size:5.5px;color:var(--muted);margin-bottom:3px}
.socials{display:flex;gap:3px;margin-top:6px}
.socials span{width:10px;height:10px;background:#3a3a3a}
.copyright{position:absolute;left:0;right:0;top:1165px;height:35px;background:#0b0b0b;text-align:center;padding-top:12px;font-size:5.5px;color:var(--muted)}
</style>
</head>
<body>
<div class="page">

  <header class="topbar">
    <div class="brand"><span class="brand-mark"></span>Quillbrook Tutorials</div>
    <div class="top-right">
      <div class="top-links"><span>Enroll Now</span><span>Contact Us</span></div>
      <div class="call">Call Us : (555) 014-2290</div>
    </div>
  </header>

  <nav class="nav">
    <a class="active">Home</a>
    <a>About Us</a>
    <a>Our Tutors</a>
    <a>Services Offered &amp; Subjects</a>
    <a>Testimonials</a>
    <a>Enroll Now / Rates</a>
    <a>QBT Locations</a>
  </nav>

  <section class="hero">
    <div class="hero-photo" role="img" aria-label="Photo of a smiling student resting her chin on her hands at a desk, with classmates studying behind her"></div>
    <div class="hero-shade"></div>
    <div class="hero-text">
      <h1>Schedule Your Free Consultation</h1>
      <p>Consultation &amp; Student Assessment</p>
      <span class="btn">Enquire Now</span>
    </div>
  </section>
  <div class="hero-rule"></div>

  <section class="services">
    <h2 class="section-title">Our Services</h2>
    <div class="sub">Daylight Walk-Home Program</div>
    <div class="service-grid">
      <div class="service">
        <div class="service-icon i-yellow"><svg viewBox="0 0 20 20"><rect x="3" y="3" width="14" height="11" rx="2" fill="#111"/><rect x="5" y="5" width="10" height="4" fill="#f6c417"/><circle cx="6" cy="16" r="2" fill="#111"/><circle cx="14" cy="16" r="2" fill="#111"/></svg></div>
        <h3>Pick-Up From School</h3>
        <p>Our staff walk each child from school to our center safely, every day of the week.</p>
        <span class="more">Read More</span>
      </div>
      <div class="service">
        <div class="service-icon i-blue"><svg viewBox="0 0 20 20"><circle cx="10" cy="10" r="7" fill="none" stroke="#fff" stroke-width="2"/><path d="M10 5v5l3 2" stroke="#fff" stroke-width="2" fill="none"/></svg></div>
        <h3>Snack Time</h3>
        <p>Children enjoy a healthy snack and a short break before study time begins each day.</p>
        <span class="more">Read More</span>
      </div>
      <div class="service">
        <div class="service-icon i-orange"><svg viewBox="0 0 20 20"><path d="M3 10l7-6 7 6v7H3z" fill="#fff"/><rect x="8" y="12" width="4" height="5" fill="#f08a1c"/></svg></div>
        <h3>Homework Help</h3>
        <p>Tutors guide students through daily homework so evenings at home stay stress free.</p>
        <span class="more">Read More</span>
      </div>
      <div class="service">
        <div class="service-icon i-teal"><svg viewBox="0 0 20 20"><rect x="4" y="3" width="12" height="14" fill="#fff"/><path d="M6 7h8M6 10h8M6 13h5" stroke="#21a3a3" stroke-width="1.5"/></svg></div>
        <h3>Enrichment Exercises</h3>
        <p>Fun worksheets and projects build skills in math, reading and problem solving.</p>
        <span class="more">Read More</span>
      </div>
    </div>
  </section>

  <section class="tutors">
    <h2 class="section-title">Our Tutors</h2>
    <div class="tutors-body">
      <p>A great tutor makes the difference in a child's learning. Our tutors are caring and certified educators who bring patience and real classroom experience to every session. They set goals with each student, track progress closely and share regular updates with parents, so families always know how their child is growing. With steady support and clear lessons, students build lasting habits that help them succeed in school and beyond. Meet our team and see how personal attention can turn struggles into strengths.</p>
      <ul class="checks">
        <li><svg viewBox="0 0 10 10"><path d="M1 5l3 3 5-6" stroke="#f6c417" stroke-width="2" fill="none"/></svg>Improve Grades</li>
        <li><svg viewBox="0 0 10 10"><path d="M1 5l3 3 5-6" stroke="#f6c417" stroke-width="2" fill="none"/></svg>Raise Test Scores</li>
        <li><svg viewBox="0 0 10 10"><path d="M1 5l3 3 5-6" stroke="#f6c417" stroke-width="2" fill="none"/></svg>Learn Problem-Solving Habits</li>
        <li><svg viewBox="0 0 10 10"><path d="M1 5l3 3 5-6" stroke="#f6c417" stroke-width="2" fill="none"/></svg>Master New Challenges</li>
        <li><svg viewBox="0 0 10 10"><path d="M1 5l3 3 5-6" stroke="#f6c417" stroke-width="2" fill="none"/></svg>Strengthen Self-Confidence</li>
      </ul>
    </div>
    <div class="bus" role="img" aria-label="Illustration of a yellow school bus"></div>
    <div class="road"></div>
  </section>

  <div class="tutor-bar">Become a Tutor - <span>Click here to fill out our online tutor inquiry form</span></div>

  <section class="lower">
    <div class="testimonial">
      <h2 class="section-title">Testimonials</h2>
      <p>"Quillbrook was a wonderful find for our family. The tutors helped both of my children grow in confidence, and their grades kept climbing all year. The walk-home program gives us real peace of mind, and we love hearing about each day's progress."</p>
      <div class="author">Marcus Ellery</div>
      <div class="author-role">Parent of College students</div>
    </div>
    <div class="schedule">
      <h2 class="section-title">Typical Daily Schedule</h2>
      <div class="tabs"><span class="on">After School Program</span><span>One-Step Program</span></div>
      <table>
        <tr><td class="time">3:00pm - 3:30pm</td><td>Pick-up from School</td></tr>
        <tr><td class="time">3:30pm - 4:00pm</td><td>Homework Help</td></tr>
        <tr><td class="time">4:00pm - 4:30pm</td><td>Snack</td></tr>
        <tr><td class="time">4:30pm - 5:30pm</td><td>Worksheets, Enrichment</td></tr>
        <tr><td class="time">5:30pm - 6:00pm</td><td>Games, Projects, Reading</td></tr>
      </table>
    </div>
  </section>

  <footer class="footer">
    <div>
      <h4>Quick Links</h4>
      <div class="links">
        <ul><li>About Us</li><li>Our Tutors</li><li>Services Offered &amp; Subjects</li><li>Testimonials</li><li>Online Enrollment</li></ul>
        <ul><li>Enroll Now / Rates</li><li>QBT Locations</li><li>Contact Us</li></ul>
      </div>
    </div>
    <div class="newsletter">
      <h4>Join Our Newsletter</h4>
      <p>Sign up for news, program updates and seasonal offers sent to your inbox.</p>
      <div class="field">Email Address</div>
      <span class="submit">Submit</span>
    </div>
    <div class="contact">
      <h4>Contact Info</h4>
      <p>42 Lantern Row, Suite 7</p>
      <p>Fairhaven, TX 70412</p>
      <p>(555) 014-2290</p>
      <p>hello@quillbrook.org</p>
      <div class="socials"><span></span><span></span><span></span><span></span></div>
    </div>
  </footer>
  <div class="copyright">Copyright © 2015 - Quillbrook. All Rights Reserved.</div>

</div>
</body>
</html>
```